Business Card For Quillmoor Financial Consulting

Hi, I would like a business card designed. Bold, modern.
Please use the same design as the logo. I have also attached the website design to see the overall theme.
Wordmark Font
Color: Hex: #01AEF7

```html
<!DOCTYPE html>
<html lang="en">
<head>
<meta charset="utf-8">
<title>Quillmoor Financial Consulting — Business Card</title>
<link href="https://fonts.googleapis.com/css2?family=Fira+Sans:wght@400;500;600;700&display=swap" rel="stylesheet">
<style>
  :root {
    --backdrop: #2a2c2f;
    --card: #13202a;
    --accent: #01aef7;
    --ink: #ffffff;
    --ink-soft: #d9e2e8;
    --rule: #6b7a85;
  }
  * { margin: 0; padding: 0; box-sizing: border-box; }
  html, body { width: 1200px; height: 874px; overflow: hidden; }
  body {
    background: var(--backdrop);
    font-family: "Fira Sans", sans-serif;
    display: flex;
    flex-direction: column;
    align-items: center;
    justify-content: center;
    gap: 40px;
  }
  .card {
    position: relative;
    width: 560px;
    height: 320px;
    background: var(--card);
    border-radius: 18px;
    border-bottom: 2px solid var(--accent);
    overflow: hidden;
  }
  .brand {
    display: flex;
    align-items: center;
    gap: 12px;
  }
  .brand-mark {
    background: var(--accent);
    flex: none;
  }
  .brand-name {
    color: var(--ink);
    font-weight: 600;
    text-transform: uppercase;
    line-height: 1.05;
    letter-spacing: 0.04em;
  }
  /* front */
  .card-front .brand {
    position: absolute;
    left: 50%; top: 50%;
    transform: translate(-50%, -50%);
  }
  .card-front .brand-mark { width: 44px; height: 44px; }
  .card-front .brand-name { font-size: 34px; }
  /* back */
  .band {
    position: absolute;
    background: var(--accent);
  }
  .band-long { left: 0; top: 56px; width: 356px; height: 30px; }
  .band-short { right: 0; top: 104px; width: 40px; height: 30px; }
  .card-back .brand {
    position: absolute;
    left: 368px; top: 66px;
    gap: 8px;
  }
  .card-back .brand-mark { width: 22px; height: 22px; }
  .card-back .brand-name { font-size: 17px; }
  .person {
    position: absolute;
    left: 34px; top: 140px;
  }
  .person-name {
    color: var(--accent);
    font-weight: 700;
    font-size: 22px;
    letter-spacing: 0.01em;
  }
  .person-title {
    color: var(--ink);
    font-size: 14px;
    font-weight: 500;
    margin-top: 2px;
  }
  .contacts {
    position: absolute;
    left: 34px; top: 206px;
    list-style: none;
  }
  .contacts li {
    display: flex;
    align-items: center;
    gap: 9px;
    color: var(--ink-soft);
    font-size: 14px;
    line-height: 22px;
  }
  .contacts svg { width: 13px; height: 13px; fill: var(--accent); flex: none; }
  .divider {
    position: absolute;
    left: 248px; top: 240px;
    width: 276px; height: 1px;
    background: var(--rule);
  }
  .address {
    position: absolute;
    right: 36px; top: 250px;
    text-align: right;
    color: var(--ink-soft);
    font-size: 14px;
    line-height: 20px;
    font-style: normal;
  }
</style>
</head>
<body>
  <section class="card card-front" aria-label="Card front">
    <div class="brand">
      <span class="brand-mark"></span>
      <span class="brand-name">Quillmoor<br>Consulting</span>
    </div>
  </section>

  <section class="card card-back" aria-label="Card back">
    <div class="band band-long"></div>
    <div class="brand">
      <span class="brand-mark"></span>
      <span class="brand-name">Quillmoor<br>Consulting</span>
    </div>
    <div class="band band-short"></div>

    <div class="person">
      <p class="person-name">MARTIN ELLISON</p>
      <p class="person-title">Managing Director</p>
    </div>

    <ul class="contacts">
      <li>
        <svg viewBox="0 0 24 24"><path d="M6.6 10.8a15.1 15.1 0 0 0 6.6 6.6l2.2-2.2a1 1 0 0 1 1-.25 11.4 11.4 0 0 0 3.6.57 1 1 0 0 1 1 1V20a1 1 0 0 1-1 1A17 17 0 0 1 3 4a1 1 0 0 1 1-1h3.5a1 1 0 0 1 1 1c0 1.25.2 2.45.57 3.6a1 1 0 0 1-.25 1z"/></svg>
        936-555-0142
      </li>
      <li>
        <svg viewBox="0 0 24 24"><path d="M7 1h10a2 2 0 0 1 2 2v18a2 2 0 0 1-2 2H7a2 2 0 0 1-2-2V3a2 2 0 0 1 2-2zm0 3v14h10V4z"/></svg>
        936-555-0187
      </li>
      <li>
        <svg viewBox="0 0 24 24"><path d="M2 5h20v14H2zm2 2v.5l8 5 8-5V7l-8 5z"/></svg>
        info@quillmoorconsulting.com
      </li>
    </ul>

    <div class="divider"></div>

    <address class="address">
      4120 Larkspur Road<br>
      Anchorage, Alaska 99507<br>
      www.quillmoorconsulting.com
    </address>
  </section>
</body>
</html>
```